Social Media Graphics - ALL TEXT RK

We are looking for a series of social media graphics for Instagram (standard size 1:1 (1080x1080px) that are ALL TEXT. We want the following quotes below on each graphic; one quote per graphic. AND, In very small letters at the bottom of each graphic, add @RKMarlowLive

The look and feel of these graphics should be complimentary to the color palette attached below; but keep them simple. But the design is up to you; at the end of this document, I provided various samples of all text graphics that I like as examples.

Target Market(s)

women looking to lose weight

Industry/Entity Type

health and wellness

Colors
E54698
E96AAD
F1A4CE
F9D9EA
FCEFF6

Requirements
Must have
• the quotes in the document
Should not have
• no stock photography

```html
<!DOCTYPE html>
<html lang="en">
<head>
<meta charset="utf-8">
<title>RK Social Quote Series</title>
<link rel="stylesheet" href="https://fonts.googleapis.com/css2?family=Bebas+Neue&family=Alegreya:wght@400&family=Poppins:wght@400&display=swap">
<style>
  :root {
    --pink-deep: #E54698;
    --pink-mid: #E96AAD;
    --pink-soft: #F1A4CE;
    --pink-pale: #F9D9EA;
    --pink-mist: #FCEFF6;
    --ink: #111111;
    --page: #FFFFFF;
  }
  * { margin: 0; padding: 0; box-sizing: border-box; }
  html, body { width: 1200px; height: 2854px; overflow: hidden; background: var(--page); }
  .sheet { position: relative; width: 1200px; height: 2854px; }
  .post {
    position: absolute;
    width: 484px; height: 484px;
    background: radial-gradient(ellipse at 50% 52%, var(--pink-mist) 0%, var(--pink-pale) 28%, var(--pink-soft) 58%, var(--pink-mid) 82%, var(--pink-deep) 100%);
  }
  .post::before {
    content: "";
    position: absolute;
    inset: 24px;
    border: 1.5px solid rgba(252, 239, 246, 0.85);
  }
  .col-left { left: 84px; }
  .col-right { left: 612px; }
  .row-1 { top: 133px; }
  .row-2 { top: 660px; }
  .row-3 { top: 1192px; }
  .row-4 { top: 1730px; }
  .row-5 { top: 2268px; }
  .quote { position: absolute; left: 46px; right: 36px; color: var(--ink); }
  .headline {
    font-family: "Bebas Neue", "Arial Narrow", sans-serif;
    font-size: 58px; line-height: 1.05; text-transform: uppercase;
  }
  .headline.large { font-size: 66px; }
  .body {
    font-family: "Alegreya", Georgia, serif;
    font-size: 30px; line-height: 1.12; text-transform: uppercase;
  }
  .body.small { font-size: 26px; }
  .handle {
    position: absolute; left: 0; right: 0; bottom: 68px;
    text-align: center;
    font-family: "Poppins", Arial, sans-serif;
    font-size: 13px; color: var(--ink);
  }
</style>
</head>
<body>
<main class="sheet">

  <section class="post col-left row-1">
    <div class="quote" style="top:104px;">
      <p class="headline">Wake up tomorrow<br>with a flatter belly</p>
      <p class="body">Yes, this overnight<br>remedy works<br>like magic!</p>
    </div>
    <p class="handle">@RKMarlowLive</p>
  </section>

  <section class="post col-right row-1">
    <div class="quote" style="top:96px;left:44px;">
      <p class="body small">Struggling with<br>bloating and belly fat?</p>
      <p class="headline" style="margin-top:4px;">Try this natural solution<br>tonight, and wake up<br>feeling lighter!</p>
    </div>
    <p class="handle">@RKMarlowLive</p>
  </section>

  <section class="post col-left row-2">
    <div class="quote" style="top:102px;left:56px;">
      <p class="headline large">One supplement,<br>one night;</p>
      <p class="body small" style="margin-left:-8px;">Your belly bloat could be<br>gone by morning.<br>Here's how it works!</p>
    </div>
    <p class="handle">@RKMarlowLive</p>
  </section>

  <section class="post col-right row-2">
    <div class="quote" style="top:100px;left:54px;">
      <p class="headline large">Finally-a natural<br>solution</p>
      <p class="body small">That flattens your belly<br>and eases stomach<br>bloat</p>
    </div>
    <p class="handle">@RKMarlowLive</p>
  </section>

  <section class="post col-left row-3">
    <div class="quote" style="top:118px;left:56px;">
      <p class="headline">Your hormones are<br>out of whack</p>
      <p class="body small" style="margin-left:-4px;">That's why the weight<br>won't budge! Sis,</p>
    </div>
    <p class="handle">@RKMarlowLive</p>
  </section>

  <section class="post col-right row-3">
    <div class="quote" style="top:92px;left:64px;">
      <p class="headline" style="font-size:44px;">Frustrated with belly fat<br>that won't budge?</p>
      <p class="body small" style="line-height:1.36;">I've got the solution<br>that finally worked<br>for me-no crazy<br>diets required.</p>
    </div>
    <p class="handle">@RKMarlowLive</p>
  </section>

  <section class="post col-left row-4">
    <div class="quote" style="top:112px;left:64px;">
      <p class="headline" style="font-size:54px;">That stubborn belly<br>fat isn't your fault</p>
      <p class="body">Here's what no<br>one tells you.</p>
    </div>
    <p class="handle">@RKMarlowLive</p>
  </section>

  <section class="post col-right row-4">
    <div class="quote" style="top:58px;left:62px;">
      <p class="body">You've been lied to</p>
      <p class="headline large" style="line-height:1.06;">Just eat less and<br>exercise more'<br>doesn't work in<br>menopause</p>
    </div>
    <p class="handle">@RKMarlowLive</p>
  </section>

  <section class="post col-left row-5">
    <div class="quote" style="top:80px;left:48px;">
      <p class="body small" style="line-height:1.1;">A natural way<br>to boost GLP-1</p>
      <p class="headline" style="font-size:60px;line-height:1.06;">No injections,<br>no side effects,<br>just real results.<br>Here's how it works</p>
    </div>
    <p class="handle">@RKMarlowLive</p>
  </section>

  <section class="post col-right row-5">
    <div class="quote" style="top:64px;left:48px;">
      <p class="headline large" style="line-height:0.98;">GLP-1: The magic<br>behind the weight<br>loss drugs.</p>
      <p class="body small" style="margin-top:8px;">But here's the secret - you<br>can boost it naturally<br>without a prescription!</p>
    </div>
    <p class="handle">@RKMarlowLive</p>
  </section>

</main>
</body>
</html>
```